Kestrel Fitness Studio Retail Tube Design

We require a design for cardboard tubes, like images included, which will be the main packaging for the clothing sold in our fitness studio. Kestrel Fitness Studio is an upscale customer service driven fitness studio that is geared towards improving our clients/members quality of life by marrying cutting edge technology like 3D scanning and metabolic measurement with first class training based on 30+ years of experience in the industry.

The project will require a design which revolves around the tube seamlessly including the lid and its top and must include the company logo, which is included, along with our web address (www.kestrelgymhall.example).

The final design should be a bold, sleek design which stands out so when people see the tube they will either know it’s from our studio or be curious as to want company it’s from. Similar to the impact the Moravanti bag has that is given to all their customers.

Target Market(s)

Individuals and groups seeking individualize fitness programs which produce results.

Industry/Entity Type

Clothing

Colors

Designer to choose colors to be used in the design.

Requirements
Must have
• Logo and website address

```html
<!DOCTYPE html>
<html lang="en">
<head>
<meta charset="utf-8">
<title>Kestrel Fitness Studio – Tube Wrap</title>
<link rel="stylesheet" href="https://fonts.googleapis.com/css2?family=Jost:wght@300;400;500;600&family=League+Spartan:wght@700;800;900&display=swap">
<style>
  :root {
    --ink: #111111;
    --paper: #ffffff;
    --accent-red: #d6283a;
    --stage: #e9ecee;
    --band-light: #f2f3f4;
    --band-mid: #c9cccf;
    --band-dark: #9ea3a7;
    --speed-line: #b9bdc1;
    --figure-tone: #eef3f5;
  }
  html, body {
    margin: 0;
    padding: 0;
    width: 1200px;
    height: 923px;
    overflow: hidden;
    background: var(--stage);
  }
  .wrap-artwork {
    position: absolute;
    left: 0;
    top: 110px;
    width: 1200px;
    height: 702px;
    display: block;
  }
  .word { fill: var(--ink); font-family: "Jost", "Futura", sans-serif; font-weight: 500; }
  .word--light { font-weight: 400; }
  .word--condensed { font-weight: 600; }
  .word--heavy { font-family: "League Spartan", "Jost", sans-serif; font-weight: 800; }
  .word--black { font-family: "League Spartan", "Jost", sans-serif; font-weight: 900; }
  .brand-name { fill: var(--ink); font-family: "League Spartan", "Jost", sans-serif; font-weight: 800; }
  .brand-square { fill: var(--accent-red); }
  .band-wordmark { fill: #2a2a2a; font-family: "Jost", sans-serif; font-weight: 300; }
  .band-tagline { fill: #2a2a2a; font-family: "Jost", sans-serif; font-weight: 400; }
  .band-url { fill: #1a1a1a; font-family: "Jost", sans-serif; font-weight: 400; }
  .speed-line { stroke: var(--speed-line); stroke-width: 2; }
</style>
</head>
<body>
<svg class="wrap-artwork" viewBox="0 0 1000 585" preserveAspectRatio="none" xmlns="http://www.w3.org/2000/svg">
  <defs>
    <linearGradient id="bandGradient" x1="0" y1="0" x2="0" y2="1">
      <stop offset="0" stop-color="var(--band-dark)"/>
      <stop offset="0.35" stop-color="var(--band-light)"/>
      <stop offset="0.75" stop-color="var(--band-mid)"/>
      <stop offset="1" stop-color="var(--band-dark)"/>
    </linearGradient>
    <clipPath id="panelClip"><rect x="0" y="0" width="1000" height="504"/></clipPath>
  </defs>

  <!-- white print panel -->
  <rect class="panel" x="0" y="0" width="1000" height="504" fill="var(--paper)"/>

  <!-- runners line-art zone -->
  <rect role="img" aria-label="Faint line drawing of running athletes behind the type" x="40" y="20" width="900" height="470" fill="var(--figure-tone)" opacity="0.55"/>

  <!-- speed lines -->
  <g class="speed-lines">
    <line class="speed-line" x1="925" y1="20" x2="990" y2="20"/>
    <line class="speed-line" x1="935" y1="32" x2="985" y2="32"/>
    <line class="speed-line" x1="925" y1="110" x2="985" y2="110"/>
    <line class="speed-line" x1="925" y1="216" x2="985" y2="216"/>
    <line class="speed-line" x1="935" y1="228" x2="990" y2="228"/>
    <line class="speed-line" x1="935" y1="245" x2="980" y2="245"/>
    <line class="speed-line" x1="940" y1="310" x2="990" y2="310"/>
    <line class="speed-line" x1="15" y1="96" x2="55" y2="96"/>
    <line class="speed-line" x1="15" y1="108" x2="60" y2="108"/>
    <line class="speed-line" x1="230" y1="200" x2="280" y2="200"/>
    <line class="speed-line" x1="15" y1="450" x2="45" y2="450"/>
    <line class="speed-line" x1="15" y1="462" x2="50" y2="462"/>
  </g>

  <!-- type collage -->
  <g class="type-collage" clip-path="url(#panelClip)">
    <text class="word word--light" x="12" y="44" font-size="44" textLength="586" lengthAdjust="spacingAndGlyphs">FITNESS.FRAMEWORK.FUNCTION</text>
    <text class="word word--condensed" x="25" y="94" font-size="38" textLength="243" lengthAdjust="spacingAndGlyphs">CARDIORESPIRATORY</text>
    <text class="word word--heavy" x="38" y="137" font-size="42" textLength="207" lengthAdjust="spacing">FITNESS</text>
    <text class="word" x="280" y="94" font-size="46" textLength="316" lengthAdjust="spacingAndGlyphs">CUTTING EDGE</text>
    <text class="word" x="280" y="139" font-size="46" textLength="316" lengthAdjust="spacingAndGlyphs">TECHNOLOGY</text>
    <text class="word word--heavy" x="630" y="48" font-size="52" textLength="282" lengthAdjust="spacingAndGlyphs">ISOKINETIC</text>
    <text class="word word--heavy" x="630" y="94" font-size="52" textLength="282" lengthAdjust="spacing">EXERCISE</text>
    <text class="word" x="627" y="134" font-size="30" textLength="358" lengthAdjust="spacingAndGlyphs">CARDIOVASCULAR SYSTEM</text>
    <text class="word" x="255" y="195" font-size="60" textLength="628" lengthAdjust="spacingAndGlyphs">FIRST CLASS TRAINING</text>
    <text class="word" x="15" y="205" font-size="50" textLength="217" lengthAdjust="spacingAndGlyphs">3D SCAN</text>
    <text class="word" x="17" y="252" font-size="50" textLength="221" lengthAdjust="spacing">YOUR</text>
    <text class="word" x="17" y="299" font-size="50" textLength="221" lengthAdjust="spacing">BODY</text>
    <text class="word word--black" x="330" y="274" font-size="96" textLength="152" lengthAdjust="spacingAndGlyphs">BMI</text>
    <text class="word" x="272" y="302" font-size="30" textLength="265" lengthAdjust="spacingAndGlyphs">BODY MASS INDEX</text>
    <text class="word word--heavy" x="570" y="268" font-size="82" textLength="262" lengthAdjust="spacingAndGlyphs">ACTIVE</text>
    <text class="word word--heavy" x="570" y="337" font-size="82" textLength="268" lengthAdjust="spacingAndGlyphs">ABILITY</text>
    <text class="word" x="15" y="347" font-size="46" textLength="540" lengthAdjust="spacingAndGlyphs">METABOLIC MEASUREMENT</text>
    <text class="word word--heavy" x="175" y="400" font-size="56" textLength="253" lengthAdjust="spacingAndGlyphs">MAXIMIZE</text>
    <text class="word word--heavy" x="175" y="447" font-size="56" textLength="243" lengthAdjust="spacingAndGlyphs">MEASURE</text>
    <text class="word word--heavy" x="175" y="494" font-size="56" textLength="247" lengthAdjust="spacingAndGlyphs">MOTIVATE</text>
    <text class="word" x="457" y="384" font-size="42" textLength="565" lengthAdjust="spacingAndGlyphs">CONCENTRIC MUSCLE ACTION</text>
    <text class="word word--light" x="435" y="424" font-size="30" textLength="130" lengthAdjust="spacing">TARGET</text>
    <text class="word word--light" x="435" y="457" font-size="30" textLength="127" lengthAdjust="spacingAndGlyphs">MUSCLES</text>
    <text class="word word--light" x="435" y="487" font-size="30" textLength="130" lengthAdjust="spacing">TRAIN</text>
    <text class="word word--heavy" x="692" y="427" font-size="46" textLength="330" lengthAdjust="spacing">HEART RATE</text>
    <text class="word word--heavy" x="692" y="464" font-size="46" textLength="330" lengthAdjust="spacing">RESERVE</text>
    <text class="word word--condensed" x="692" y="497" font-size="34" textLength="345" lengthAdjust="spacingAndGlyphs">BREATHE.BALANCE</text>

    <!-- brand name marks -->
    <g class="brand-mark">
      <rect class="brand-square" x="50" y="436" width="16" height="16"/>
      <text class="brand-name" x="72" y="452" font-size="24" textLength="88" lengthAdjust="spacingAndGlyphs">KESTREL</text>
    </g>
    <g class="brand-mark">
      <rect class="brand-square" x="570" y="436" width="16" height="16"/>
      <text class="brand-name" x="592" y="452" font-size="24" textLength="88" lengthAdjust="spacingAndGlyphs">KESTREL</text>
    </g>
  </g>

  <!-- silver footer band -->
  <g class="footer-band">
    <rect x="0" y="504" width="1000" height="81" fill="url(#bandGradient)"/>
    <text class="band-wordmark" x="8" y="558" font-size="50" textLength="214" lengthAdjust="spacingAndGlyphs">Kestrel</text>
    <text class="band-tagline" x="38" y="577" font-size="13" textLength="152" lengthAdjust="spacing">FITNESS STUDIO</text>
    <text class="band-url" x="257" y="553" font-size="20" textLength="165" lengthAdjust="spacingAndGlyphs">kestrelgymhall.example</text>
    <text class="band-wordmark" x="525" y="558" font-size="50" textLength="214" lengthAdjust="spacingAndGlyphs">Kestrel</text>
    <text class="band-tagline" x="555" y="577" font-size="13" textLength="152" lengthAdjust="spacing">FITNESS STUDIO</text>
    <text class="band-url" x="783" y="553" font-size="20" textLength="165" lengthAdjust="spacingAndGlyphs">kestrelgymhall.example</text>
  </g>
</svg>
</body>
</html>
```